New Content Rich Website Designs

We need an updated design layout for our website that is content rich.  Attached please find a document named Web Designer Instructions and also a New Home Page.   We are looking for your new fresh ideas on how to make our website communicate what our company does and make us stand out from the rest but is inviting.    We are looking for our new website to be Wordpress.  Our current website is at https://www.vr-harbor.com/ which we are only providing as a reference guide.
VR Harbor Builds and Manages Custom Single-Family Offices please review our website and the New Home Page & Web Designer Instructions for more details. Color scheme -  we would like to follow the same color scheme as our current website.  Provided logo samples as well.

Coding
Coded - Design and coding required
Number of Pages Required
5+ page
Colors
Designer to choose colors to be used in the design.
Requirements
Must have
- 4 P's / Floating Navigation Bar /Stick to the Script

```html
<!DOCTYPE html>
<html lang="en">
<head>
<meta charset="utf-8">
<title>VR Harbor — Bespoke Family Office Solutions</title>
<link href="https://fonts.googleapis.com/css2?family=Playfair+Display:wght@500;600;700&family=Inter:wght@400;500;600;700&display=swap" rel="stylesheet">
<style>
:root{
  --navy:#1c3466;
  --navy-dark:#142750;
  --blue:#2d5fd9;
  --blue-soft:#e9eff9;
  --ink:#1d2433;
  --muted:#5d6678;
  --line:#d7deea;
  --white:#ffffff;
  --grey:#dfe2e7;
}
*{box-sizing:border-box;margin:0;padding:0}
html,body{width:1200px;height:5148px;overflow:hidden}
body{font-family:"Inter",Arial,sans-serif;color:var(--ink);background:var(--white);font-size:13px;line-height:1.55}
h1,h2,h3,.serif{font-family:"Playfair Display",Georgia,serif;font-weight:600}
.btn{display:inline-block;padding:9px 18px;border-radius:4px;font-size:12px;font-weight:600;border:1px solid transparent}
.btn-navy{background:var(--navy);color:var(--white)}
.btn-outline{border-color:var(--navy);color:var(--navy);background:var(--white)}
.btn-white{background:var(--white);color:var(--navy)}
.btn-ghost{border-color:var(--white);color:var(--white)}

/* hero */
.hero{position:relative;height:660px;background:linear-gradient(180deg,#e9eaec 0%,#cfd2d7 45%,#f1f2f3 100%);text-align:center}
.hero-photo{position:absolute;inset:0;background:radial-gradient(ellipse at 50% 50%,#fafafa 0%,#d6d8dc 45%,#aeb2b8 100%)}
.nav{position:absolute;top:0;left:0;right:0;height:46px;display:flex;align-items:center;padding:0 30px;background:rgba(255,255,255,.85)}
.brand{display:flex;align-items:center;gap:8px;font-weight:700;font-size:14px;color:var(--navy)}
.brand .dot{width:22px;height:22px;border-radius:50%;background:var(--navy)}
.nav ul{list-style:none;display:flex;gap:20px;margin-left:auto;margin-right:26px;font-size:11px;color:var(--ink)}
.nav li.active{color:var(--navy);font-weight:600;border-bottom:2px solid var(--navy)}
.hero-copy{position:absolute;top:388px;left:0;right:0}
.hero h1{font-size:44px;line-height:1.15;color:var(--ink)}
.hero p{font-size:12px;color:var(--muted);margin:12px 0 20px}
.hero .btn+.btn{margin-left:10px}

/* about */
.about{position:relative;height:660px;background:var(--white)}
.about-wave{position:absolute;left:0;right:0;top:420px}
.about-circle{position:absolute;left:150px;top:60px;width:300px;height:300px;border-radius:50%;border:10px solid var(--navy);background:linear-gradient(135deg,#8ea6c8,#415e8e)}
.about-text{position:absolute;left:610px;top:66px;width:420px}
.about-text h2{font-size:26px;margin-bottom:14px;color:var(--ink)}
.about-text p{font-size:11.5px;color:var(--muted);margin-bottom:12px}

/* how */
.how{position:relative;height:240px;background:var(--blue-soft);text-align:center}
.how h2{font-size:28px;padding-top:26px}
.steps{position:absolute;top:90px;left:100px;right:100px;display:flex;justify-content:space-between}
.step{width:300px;position:relative}
.step .num{font-family:"Playfair Display",serif;font-size:64px;color:var(--white);line-height:1;text-shadow:0 0 1px #b9c5da}
.step h3{font-size:15px;margin-top:-6px}
.step p{font-size:10.5px;color:var(--muted);margin-top:4px}
.steps svg{position:absolute;top:30px}

/* feature */
.feature{position:relative;height:640px;background:var(--white)}
.watermark{position:absolute;top:-26px;left:0;right:0;text-align:center;font-family:"Inter",sans-serif;font-weight:700;font-size:76px;letter-spacing:4px;color:transparent;-webkit-text-stroke:1px #d9dde6}
.feature-photo{position:absolute;left:150px;top:40px;width:900px;height:440px;background:linear-gradient(160deg,#f2f2f2 0%,#b9bcc1 50%,#4d5158 100%)}
.play{position:absolute;left:573px;top:170px}
.feature-box{position:absolute;left:250px;top:240px;width:700px;height:220px;background:var(--navy);color:var(--white);text-align:center;padding:56px 70px 0}
.feature-box h2{font-size:30px;margin-bottom:12px}
.feature-box p{font-size:11px;opacity:.85}
.awards{position:absolute;top:520px;left:160px;right:160px;display:flex;justify-content:space-between;align-items:center}
.award{width:110px;height:70px;background:#e4e7ee}
.award.round{width:70px;border-radius:50%}
.award.shield{width:70px;border-radius:8px 8px 35px 35px;background:var(--navy)}

/* anatomy */
.anatomy{height:680px;background:var(--white);text-align:center;padding-top:24px}
.anatomy h2{font-size:26px;margin-bottom:22px}
.sfo-table{width:900px;margin:0 auto;border-collapse:collapse;text-align:left;font-size:11.5px}
.sfo-table th{background:var(--navy);color:var(--white);padding:20px 22px;font-size:13px;font-weight:600}
.sfo-table td{padding:30px 22px;border-bottom:1px solid var(--line);color:var(--muted)}
.sfo-table td:first-child{font-weight:600;color:var(--ink);width:160px}
.sfo-table tr:nth-child(even) td{background:var(--blue-soft)}

/* stats */
.stats{height:220px;background:linear-gradient(90deg,var(--navy-dark),var(--navy));display:flex;justify-content:space-around;align-items:center;padding:0 80px;color:var(--white)}
.stat b{display:block;font-family:"Playfair Display",serif;font-size:40px;font-weight:600;line-height:1.1}
.stat span{font-size:13px;opacity:.85}

/* testimonial */
.testimonial{position:relative;height:560px;background:var(--white)}
.testimonial-card{position:absolute;left:110px;top:60px;width:980px;height:440px;background:linear-gradient(135deg,#f7f9fc,#e8eef8)}
.client-mark{position:absolute;left:170px;top:120px;width:330px;height:330px;border-radius:50%;background:linear-gradient(135deg,#3a5488,#1c3466)}
.quote{position:absolute;left:630px;top:120px;width:380px}
.quote blockquote{font-family:"Playfair Display",serif;font-size:24px;line-height:1.35;color:var(--navy)}
.quote cite{display:block;font-style:normal;font-size:10.5px;color:var(--muted);margin-top:10px}
.qmark{font-family:"Playfair Display",serif;font-size:90px;color:var(--navy);line-height:1;position:absolute}
.reviews-btn{position:absolute;left:530px;top:460px}
.arrow{position:absolute;top:290px;font-size:20px;color:#9aa4b8}

/* faq */
.faq{height:470px;background:#f3f5f9;text-align:center;padding-top:30px}
.faq h2{font-size:26px;margin-bottom:20px}
.faq-list{width:740px;margin:0 auto;text-align:left}
.faq-item{background:var(--white);border:1px solid var(--line);padding:10px 18px;font-size:11px;margin-bottom:8px;display:flex;justify-content:space-between}
.faq-item.open{display:block;background:var(--navy);color:var(--white);padding:12px 18px 14px}
.faq-item.open h3{font-family:"Inter",sans-serif;font-size:12px;font-weight:600;margin-bottom:8px}
.faq-item.open p{font-size:10.5px;opacity:.85;background:var(--white);color:var(--muted);padding:8px 10px;margin:0 -6px}
.faq .btn{margin-top:14px}

/* insights */
.insights{height:650px;background:var(--white);text-align:center;padding-top:30px}
.insights h2{font-size:28px;margin-bottom:26px}
.cards{display:flex;gap:28px;justify-content:center}
.card{width:300px;text-align:left}
.card .thumb{height:250px}
.card h3{font-size:18px;margin:16px 0 8px;line-height:1.2}
.card p{font-size:10.5px;color:var(--muted);margin-bottom:12px}

/* cta */
.cta{height:200px;background:var(--blue);color:var(--white);text-align:center;padding-top:44px}
.cta h2{font-size:30px}
.cta p{font-size:11.5px;opacity:.9;margin:6px 0 16px}
.cta .btn+.btn{margin-left:10px}

/* footer */
.footer{height:168px;background:var(--navy-dark);color:#c9d2e4;display:flex;gap:50px;padding:26px 70px 0;font-size:10.5px;position:relative}
.footer h4{color:var(--white);font-size:12px;margin-bottom:8px}
.footer ul{list-style:none}
.footer li{margin-bottom:4px;display:flex;align-items:center;gap:6px}
.footer .ico{width:14px;height:14px;border-radius:50%;background:var(--blue)}
.footer .brand{color:var(--white)}
.footer .brand .dot{background:var(--white)}
.sub{display:flex;margin-top:8px}
.sub span{background:var(--white);color:var(--muted);padding:6px 10px;width:150px}
.sub b{background:var(--blue);color:var(--white);padding:6px 10px}
.copyright{position:absolute;bottom:8px;left:0;right:0;text-align:center;font-size:9.5px;opacity:.7}
</style>
</head>
<body>

<header class="hero">
  <div class="hero-photo" role="img" aria-label="Grey architectural interior receding into perspective"></div>
  <nav class="nav">
    <div class="brand"><span class="dot"></span>VR Harbor</div>
    <ul><li class="active">Home</li><li>About Us</li><li>Our Services</li><li>Why VR Harbor</li><li>Insights</li><li>Contact</li></ul>
    <span class="btn btn-navy">Request a Consultation</span>
  </nav>
  <div class="hero-copy">
    <h1>Bespoke Family Office Solutions<br>for Generational Impact</h1>
    <p>Custom single-family office solutions for families with complex financial, legal, and business needs.</p>
    <span class="btn btn-navy">Request a Consultation</span><span class="btn btn-outline">What is a Family Office?</span>
  </div>
</header>

<section class="about">
  <svg class="about-wave" width="1200" height="120" viewBox="0 0 1200 120"><path d="M0 80 C300 0 700 140 1200 30" fill="none" stroke="#dbe3f1" stroke-width="2"/></svg>
  <div class="about-circle" role="img" aria-label="Team of advisers gathered around a globe"></div>
  <div class="about-text">
    <h2>About VR Harbor</h2>
    <p>After leading significant Single Family Offices, we founded VR Harbor in 2017 to fill a critical gap in the wealth management landscape – many families of substantial net worth remain unsupported, lacking bespoke guidance.</p>
    <p>Many aspire to establish their own well-staffed SFO but recognize the significant cost, strategic value, and complexities of managing one independently. At the same time, high-end Multi-Family Offices often fall short, unable to provide the control, customized, and aligned incentives and independence that a true SFO offers.</p>
    <span class="btn btn-navy">Learn More About Us</span>
  </div>
</section>

<section class="how">
  <h2>How We Work</h2>
  <div class="steps">
    <div class="step"><div class="num">01.</div><h3>Strategic Assessment</h3><p>We begin with deep conversations to un-<br>derstand your family's structure, wealth</p></div>
    <svg style="left:300px" width="100" height="20"><path d="M0 10 C30 0 70 20 96 10" stroke="#1c3466" fill="none"/><path d="M90 6 L97 10 L90 14" stroke="#1c3466" fill="none"/></svg>
    <div class="step"><div class="num">02.</div><h3>Family Office Design</h3><p>We architect your office from the ground up<br>– structuring governance, legal frameworks,</p></div>
    <svg style="left:600px" width="100" height="20"><path d="M0 10 C30 0 70 20 96 10" stroke="#1c3466" fill="none"/><path d="M90 6 L97 10 L90 14" stroke="#1c3466" fill="none"/></svg>
    <div class="step"><div class="num">03.</div><h3>Implementation &amp; Setup</h3><p>We coordinate &amp; oversee the operational build-<br>out – from hiring &amp; onboarding to technology</p></div>
  </div>
</section>

<section class="feature">
  <div class="watermark">VR HARBOR</div>
  <div class="feature-photo" role="img" aria-label="White modern architecture with curved ceiling beams"></div>
  <svg class="play" width="54" height="54"><circle cx="27" cy="27" r="26" fill="#fff" opacity=".9"/><path d="M22 17 L37 27 L22 37Z" fill="#1c3466"/></svg>
  <div class="feature-box">
    <h2>What is a Family Office?</h2>
    <p>VR Harbor was founded by seasoned single family office executives with the rare expertise of building and managing the family offices of some of the world's wealthiest families. With decades of experience, we have advised high-net-worth families and directly managed across multiple asset classes, market cycles, and bespoke investment opportunities tailored for substantial wealth.</p>
  </div>
  <div class="awards">
    <div class="award round"></div>
    <div class="award"></div>
    <div class="award round"></div>
    <div class="award shield"></div>
    <div class="award"></div>
  </div>
</section>

<section class="anatomy">
  <h2>Anatomy of a True SFO</h2>
  <table class="sfo-table">
    <tr><th>Feature</th><th>Single-Family Office (SFO)</th><th>Multi-Family Office (MFO)</th></tr>
    <tr><td>Ownership</td><td>Owned and operated by one family</td><td>Serves multiple unrelated families</td></tr>
    <tr><td>Customization</td><td>Fully bespoke, built around one family's needs</td><td>Standardized services across client base</td></tr>
    <tr><td>Control</td><td>Full control over staff, strategy, and governance</td><td>Limited control, shared resources</td></tr>
    <tr><td>Cost</td><td>Higher upfront investment, scalable over time</td><td>Lower cost to entry, but limited flexibility</td></tr>
    <tr><td>Service Scope</td><td>Tailored across financial, legal, lifestyle, legacy</td><td>Focused primarily on financial/investment services</td></tr>
    <tr><td>Team Structure</td><td>Custom-hired and managed directly by the family</td><td>Provided and managed by the MFO firm</td></tr>
  </table>
</section>

<section class="stats">
  <div class="stat"><b>15+</b><span>years experience</span></div>
  <div class="stat"><b>100%</b><span>tailored solutions</span></div>
  <div class="stat"><b>20+</b><span>Countries Clients</span></div>
  <div class="stat"><b>1,200+</b><span>team of experts</span></div>
</section>

<section class="testimonial">
  <div class="testimonial-card"></div>
  <span class="arrow" style="left:60px">&#8592;</span><span class="arrow" style="right:60px">&#8594;</span>
  <div class="client-mark" role="img" aria-label="Client emblem placeholder"></div>
  <span class="qmark" style="left:575px;top:100px">&ldquo;</span>
  <div class="quote">
    <blockquote>VR Harbor delivered a SFO structure in weeks that had stumped our legacy advisers for years. Our family trust now works—and we have real second generation participation.</blockquote>
    <cite>— Family Principal, North America</cite>
  </div>
  <span class="qmark" style="left:1020px;top:350px">&rdquo;</span>
  <span class="btn btn-navy reviews-btn">View All Reviews</span>
</section>

<section class="faq">
  <h2>Major Landing Pages Preview</h2>
  <div class="faq-list">
    <div class="faq-item open"><h3>What is a single-family office?</h3><p>A single-family office (SFO) is a private entity established to manage the financial, legal, and personal affairs of one ultra-high-net-worth family. It can include investment management, tax, governance, succession planning, and lifestyle support — tailored exclusively to the family's needs.</p></div>
    <div class="faq-item"><span>How is VR Harbor different from other advisors or firms?</span><span>&#8964;</span></div>
    <div class="faq-item"><span>Who typically engages VR Harbor?</span><span>&#8964;</span></div>
    <div class="faq-item"><span>Do you manage investments directly?</span><span>&#8964;</span></div>
    <div class="faq-item"><span>Can you work with our existing advisors?</span><span>&#8964;</span></div>
  </div>
  <span class="btn btn-navy">View All FAQ</span>
</section>

<section class="insights">
  <h2>Latest Insights</h2>
  <div class="cards">
    <article class="card">
      <div class="thumb" role="img" aria-label="Advisers in a meeting room reviewing documents" style="background:linear-gradient(135deg,#9a8f83,#4b4a4e)"></div>
      <h3>Traditional RIAs and Multi Family Offices</h3>
      <p>Most wealth management firms offer broad services, strong judgment and quality. Yet most operate with one model and a shared team.</p>
      <span class="btn btn-navy">Read More</span>
    </article>
    <article class="card">
      <div class="thumb" role="img" aria-label="Bank building facade with signage" style="background:linear-gradient(135deg,#c7ced8,#5e6a7c)"></div>
      <h3>Private banks</h3>
      <p>Banks guide a portfolio of interest and product sourcing mandates. They can only assist with their own offerings and lending needs.</p>
      <span class="btn btn-navy">Read More</span>
    </article>
    <article class="card">
      <div class="thumb" role="img" aria-label="Team seated at a boardroom table" style="background:linear-gradient(135deg,#b8a48c,#5a4a3d)"></div>
      <h3>OCIO<sup>*</sup> firms</h3>
      <p>Outsourced officers tend to focus on the family's investment portfolio and its long-term strategy, and can lack broader office services.</p>
      <span class="btn btn-navy">Read More</span>
    </article>
  </div>
</section>

<section class="cta">
  <h2>Ready to Design a Family Office That Reflects Your Legacy?</h2>
  <p>We help exceptional families around the world create bespoke single-family offices — built for long-term growth, alignment, and impact.</p>
  <span class="btn btn-white">Speak With VR Harbor</span><span class="btn btn-ghost">Download White Paper</span>
</section>

<footer class="footer">
  <div style="width:180px">
    <div class="brand"><span class="dot"></span>VR Harbor</div>
    <p style="margin-top:10px">After leading significant Single Family Offices, we founded VR Harbor in 2017 to address a critical gap in wealth.</p>
  </div>
  <div><h4>Quick Links</h4><ul><li>About Us</li><li>Why VR Harbor</li><li>Insights</li><li>Contact</li></ul></div>
  <div><h4>Contact Us</h4><ul><li><span class="ico"></span>220 Harbor Lane, Suite 4</li><li><span class="ico"></span>+1 (555) 014-2288</li><li><span class="ico"></span>info@vr-harbor.com</li></ul></div>
  <div><h4>Community</h4><ul><li><span class="ico"></span>Events</li><li><span class="ico"></span>Podcast</li><li><span class="ico"></span>Journal</li><li><span class="ico"></span>Careers</li></ul></div>
  <div><h4>Subscribe Newsletter</h4><p>Subscribe to our newsletter</p><div class="sub"><span>Enter email...</span><b>&#8594;</b></div></div>
  <div class="copyright">© 2025 VR Harbor. All rights reserved.</div>
</footer>

</body>
</html>
```